Construction Company Website Design

I need a Website Design for a Construction Company. I have attached logo and business card design files (a.i) to match styles and text for the website. I will need design for 3 pages:
1. A Home page
2. A secondary page (will be different information pages)
3. A contact page with submision form
Website to look professional and match the 'theme' across all pages, using main colours / reverse colours as per design files. Must be clear it is a construction related website without being over the top. Happy for the construction related details (whether that be images/outlines/backgrounds etc to be fairly subtle and not overbearing on the contect of the pages. It will be the content that will be most important, not the images within.

Content has not yet been fully completed but attached is a site map. Each page will need a space for the insertion of the relevant heading and associated content for that particular page. Example can be used as per attached map. If it is preferable to have content completed for this to be a more succesful project please advise and I will complete and submit.

Target Market(s)

Clients for potential construction projects. These could be a range of people. All would be very professional, well educated and put a substantial expection on the quality of website provided.

Industry/Entity Type

Construction

Number of Pages Required

3 page

Font styles to use
Serif
Sans Serif
Other font styles liked:
• fonts preferable as per design files provided unless designer beleives a different font would suit better

Requirements
Must have
• Colour scheme to match logo and business card files provided. Fonts that match as per provided files. Pages must be consistent with the theme carrying across all pages. All pages must have contact details at the bottom of the page.
• Contents of page 1 - 'Home page': multiple tab options / logo link
• Contents of page 2 - 'Secondary page': Top and side navigation / area for information and/or images.
• Contents of page - 'Contact us page': Top and side navigation / Submission form / area for logos such as linkdin, facebook etc.
Nice to have
• Would be good to have a or some generic construction related images - outlines / shadows / effects etc. These might be background images or outlines related to the relevant industry and are consistent across the pages. Could be outlines of buildings, images of men with hardhats etc etc. Good to see colour scheme as per design files used
Should not have
• No pictures of houses. Generally no photos. If any imagery of people must not show faces/details.

```html
<!DOCTYPE html>
<html lang="en">
<head>
<meta charset="utf-8">
<title>Norvane Constructions</title>
<link href="https://fonts.googleapis.com/css2?family=Roboto:wght@300;400;500;700&display=swap" rel="stylesheet">
<style>
:root{
  --sky:#7cc6e6;
  --sky-end:#a7bcc9;
  --accent:#14a9e6;
  --charcoal:#49494b;
  --charcoal-dark:#3a3a3c;
  --paper:#dedddb;
  --card:#ffffff;
  --ink:#222222;
  --brand-ink:#3c4a55;
  --btn:#4a4a4a;
  --blueprint:#1f7fd0;
  --blueprint-dark:#1766b3;
  --night:#0b0c14;
  --field:#c5e0f7;
  --white:#ffffff;
}
*{box-sizing:border-box;margin:0;padding:0}
html,body{width:1200px;height:2174px;overflow:hidden}
body{font-family:"Roboto",Arial,sans-serif;color:var(--ink);background:var(--paper)}
.page{position:relative;width:1200px;height:2174px;overflow:hidden}

/* header */
.site-header{position:absolute;left:0;top:0;width:1200px;height:148px;background:linear-gradient(90deg,var(--sky),var(--sky-end))}
.social{position:absolute;left:161px;top:32px;display:flex;gap:14px}
.social span{width:28px;height:28px;border-radius:50%;background:rgba(255,255,255,.85)}
.brand{position:absolute;left:432px;top:30px;width:380px;text-align:center;font-size:28px;font-weight:400;color:var(--brand-ink);white-space:nowrap}
.header-phone{position:absolute;left:900px;top:32px;font-size:22px;font-weight:300;color:var(--white)}
.main-nav{position:absolute;left:0;top:114px;width:1200px;display:flex;justify-content:center;gap:28px;font-size:13px;font-weight:500}
.main-nav a{color:var(--white);text-decoration:none}
.main-nav a.current{color:#111}

/* hero */
.hero{position:absolute;left:0;top:148px;width:1200px;height:403px;background:var(--charcoal)}
.skyline{position:absolute;left:116px;top:214px;width:956px;height:189px;background:linear-gradient(180deg,#555557,var(--charcoal-dark))}
.hero h1{position:absolute;left:0;top:80px;width:1200px;text-align:center;color:var(--white);font-size:29px;font-weight:700}
.hero h2{position:absolute;left:0;top:124px;width:1200px;text-align:center;color:var(--white);font-size:23px;font-weight:700}
.hl{color:var(--accent)}
.hero p{position:absolute;left:235px;top:178px;width:730px;text-align:center;color:var(--white);font-size:14px;line-height:23px}
.hero-btn{position:absolute;left:485px;top:281px;width:229px;height:40px;border:2px solid var(--accent);border-radius:3px;background:var(--charcoal-dark);color:var(--white);font-size:11px;font-weight:500;display:flex;align-items:center;justify-content:center}

/* projects */
.projects{position:absolute;left:0;top:551px;width:1200px;height:1051px;background:var(--paper)}
.section-title{position:absolute;left:0;width:1200px;text-align:center;font-size:26px;font-weight:500}
.projects .section-title{top:44px;color:#222}
.title-rule{position:absolute;height:1px;background:#fff}
.card{position:absolute;width:266px;height:428px;background:var(--card);border:2px solid #5a5a5a;border-radius:3px;overflow:hidden;text-align:center}
.card-image{height:210px;background:linear-gradient(180deg,var(--blueprint),var(--blueprint-dark))}
.card h3{margin:10px 40px 0;font-size:12px;font-weight:700;line-height:22px;height:66px;letter-spacing:.3px}
.card dl{font-size:11.5px;line-height:18px;margin-top:6px}
.card dt{display:inline;font-weight:700}
.card dd{display:inline}
.card dd::after{content:"";display:block}
.card-btn{display:block;margin:12px auto 0;width:167px;height:38px;line-height:38px;background:var(--btn);color:var(--white);font-size:10px;font-weight:500;border-radius:3px}
.card-btn.active{background:var(--accent);border:2px solid #0b6fa6;line-height:34px}

/* contact */
.contact{position:absolute;left:0;top:1602px;width:1200px;height:516px;background:var(--night);color:var(--white)}
.contact-backdrop{position:absolute;inset:0;background:radial-gradient(ellipse at center,#0a0a10 25%,#14163e 70%,#1d2a8a 100%)}
.contact .section-title{top:40px;color:var(--white)}
.field-label{position:absolute;font-size:17px;font-weight:500}
.field{position:absolute;height:34px;width:241px;background:var(--field);border-radius:2px;color:#a9c4dc;font-size:12px;padding:10px 19px}
.field.area{height:105px;width:372px}
.check{position:absolute;left:449px;top:418px;width:24px;height:24px;background:var(--field);border-radius:2px}
.submit{position:absolute;left:762px;top:408px;width:228px;height:43px;background:var(--accent);color:var(--white);font-size:18px;font-weight:500;display:flex;align-items:center;justify-content:center;border-radius:2px}

/* footer */
.site-footer{position:absolute;left:0;top:2118px;width:1200px;height:56px;background:#101116;color:var(--white);font-size:12px}
.site-footer .item{position:absolute;top:20px}
</style>
</head>
<body>
<div class="page">

  <header class="site-header">
    <div class="social" aria-label="Social links"><span></span><span></span><span></span><span></span></div>
    <div class="brand">Norvane Constructions</div>
    <div class="header-phone">555-014-2278</div>
    <nav class="main-nav">
      <a href="#">HOME</a><a href="#" class="current">ABOUT US</a><a href="#">SERVICES</a><a href="#">PROJECTS</a><a href="#">CULTURE</a><a href="#">NEWS</a><a href="#">CONTACT</a>
    </nav>
  </header>

  <section class="hero">
    <div class="skyline" role="img" aria-label="Subtle outline of a city skyline"></div>
    <h1>Welcome To <span class="hl">Norvane Constructions</span></h1>
    <h2>Our <span class="hl">Mission</span></h2>
    <p>Our business mission is to provide our customers with first-class products at an affordable price. Our business concept leverages technology to develop products with functions superior to conventional versions in alignment with our mission of delivering exceptional value to our customers.</p>
    <div class="hero-btn">MORE ABOUT THE COMPANY</div>
  </section>

  <section class="projects">
    <div class="title-rule" style="left:384px;top:61px;width:130px"></div>
    <div class="title-rule" style="left:689px;top:61px;width:130px"></div>
    <h2 class="section-title">Our <span class="hl">Projects</span></h2>

    <article class="card" style="left:181px;top:111px">
      <div class="card-image" role="img" aria-label="Blueprint drawing of a house elevation"></div>
      <h3>Lorem ipsum dolor sit amet, consectetur adipiscing elit</h3>
      <dl><dt>Address:</dt> <dd>ed dictum, ipsum volutpat luctus</dd><dt>Region:</dt> <dd>ipsum volutpat luctus</dd><dt>Date:</dt> <dd>2018-02-20</dd><dt>Price:</dt> <dd>10000$</dd></dl>
      <span class="card-btn">LEARN MORE</span>
    </article>
    <article class="card" style="left:465px;top:111px">
      <div class="card-image" role="img" aria-label="Blueprint sketch of two residential towers"></div>
      <h3>Suspendisse nisi quam, gravida id malesuada et, imperdiet in lorem.</h3>
      <dl><dt>Address:</dt> <dd>ed dictum, ipsum volutpat luctus</dd><dt>Region:</dt> <dd>ipsum volutpat luctus</dd><dt>Date:</dt> <dd>2018-02-20</dd><dt>Price:</dt> <dd>24000$</dd></dl>
      <span class="card-btn active">LEARN MORE</span>
    </article>
    <article class="card" style="left:749px;top:111px">
      <div class="card-image" role="img" aria-label="Blueprint drawing of a house elevation"></div>
      <h3>Lorem ipsum dolor sit amet, consectetur adipiscing elit</h3>
      <dl><dt>Address:</dt> <dd>ed dictum, ipsum volutpat luctus</dd><dt>Region:</dt> <dd>ipsum volutpat luctus</dd><dt>Date:</dt> <dd>2018-02-20</dd><dt>Price:</dt> <dd>15000$</dd></dl>
      <span class="card-btn">LEARN MORE</span>
    </article>

    <article class="card" style="left:181px;top:563px">
      <div class="card-image" role="img" aria-label="Blueprint sketch of two residential towers"></div>
      <h3>Lorem ipsum dolor sit amet, consectetur adipiscing elit</h3>
      <dl><dt>Address:</dt> <dd>ed dictum, ipsum volutpat luctus</dd><dt>Region:</dt> <dd>ipsum volutpat luctus</dd><dt>Date:</dt> <dd>2018-02-20</dd><dt>Price:</dt> <dd>10500$</dd></dl>
      <span class="card-btn">LEARN MORE</span>
    </article>
    <article class="card" style="left:465px;top:563px">
      <div class="card-image" role="img" aria-label="Blueprint drawing of a house elevation"></div>
      <h3>Lorem ipsum dolor sit amet, consectetur adipiscing elit</h3>
      <dl><dt>Address:</dt> <dd>ed dictum, ipsum volutpat luctus</dd><dt>Region:</dt> <dd>ipsum volutpat luctus</dd><dt>Date:</dt> <dd>2018-02-20</dd><dt>Price:</dt> <dd>10000$</dd></dl>
      <span class="card-btn">LEARN MORE</span>
    </article>
    <article class="card" style="left:749px;top:563px">
      <div class="card-image" role="img" aria-label="Blueprint drawing of a house elevation"></div>
      <h3>Lorem ipsum dolor sit amet, consectetur adipiscing elit</h3>
      <dl><dt>Address:</dt> <dd>ed dictum, ipsum volutpat luctus</dd><dt>Region:</dt> <dd>ipsum volutpat luctus</dd><dt>Date:</dt> <dd>2018-02-20</dd><dt>Price:</dt> <dd>20000$</dd></dl>
      <span class="card-btn">LEARN MORE</span>
    </article>
  </section>

  <section class="contact">
    <div class="contact-backdrop" role="img" aria-label="Dark perspective view of a steel building frame in blue light"></div>
    <div class="title-rule" style="left:386px;top:57px;width:136px;background:#8a8fa8"></div>
    <div class="title-rule" style="left:688px;top:57px;width:136px;background:#8a8fa8"></div>
    <h2 class="section-title">Contact <span class="hl">Us</span></h2>

    <span class="field-label" style="left:209px;top:136px">First Name:</span>
    <div class="field" style="left:322px;top:128px">First name</div>
    <span class="field-label" style="left:638px;top:136px">Last Name:</span>
    <div class="field" style="left:749px;top:128px">Last Name</div>

    <span class="field-label" style="left:209px;top:208px">E-Mail:</span>
    <div class="field" style="left:322px;top:200px">E-Mail</div>
    <span class="field-label" style="left:638px;top:208px">Phone:</span>
    <div class="field" style="left:749px;top:200px">Phone</div>

    <span class="field-label" style="left:309px;top:282px">Comments/Questions:</span>
    <div class="field area" style="left:530px;top:274px"></div>

    <span class="field-label" style="left:210px;top:418px">Sign up for our Newsletter</span>
    <div class="check"></div>
    <div class="submit">SUBMIT</div>
  </section>

  <footer class="site-footer">
    <span class="item" style="left:316px">Copyright © <span class="hl">Norvane Constructions</span></span>
    <span class="item" style="left:553px">phone: 555-014-2278</span>
    <span class="item" style="left:727px">email: hello@norvanebuild.com</span>
  </footer>

</div>
</body>
</html>
```